Service Plan Sales Flyer

The Watchpost Depot (www.kelvamart.com) is a commercial security integrator that installs security cameras, access control, intrusion, two-way radios and perimeter security. We require a one page flyer for our service plan for new and existing customers. The price of the service plan is $299/yr and includes the following;
1. Discounted service rate of $118/hr
2. Free remote support ($85/hr without a plan)
3. Free remote training
4. Priority support

Please review our brochure attached and create a one page sales flyer with the end goal of having the client sign up for our annual service plan . The plan will automatically renew every year. Email sales@kelvamart.com.

Target Market(s)

commercial industrial clients - no residential

Industry/Entity Type

review our website at www.kelvamart.com

Colors
0054AA
0677BA
7BADD7
CADEEF
E8F1F8
EE7325
F08F49
F5BC92
FAE3D3
FDF4ED

Requirements
Must have
• call to action
Should not have
• too many colors

```html
<!DOCTYPE html>
<html lang="en">
<head>
<meta charset="utf-8">
<title>The Watchpost Depot – Service Plan</title>
<link rel="stylesheet" href="https://fonts.googleapis.com/css2?family=Montserrat:wght@700;800&display=swap">
<style>
  :root {
    --navy: #1f2d4f;
    --red: #e8443d;
    --white: #ffffff;
    --paper: #f7f7f8;
    --photo-light: #eef0f3;
    --photo-dark: #c9ced6;
  }
  * { margin: 0; padding: 0; box-sizing: border-box; }
  html, body { width: 849px; height: 1200px; overflow: hidden; }
  body { font-family: "Montserrat", Arial, sans-serif; background: var(--white); }

  .flyer { position: relative; width: 849px; height: 1200px; background: var(--paper); overflow: hidden; }

  .brand { display: flex; align-items: center; justify-content: center; gap: 14px; }
  .brand-mark { width: 30px; height: 30px; background: var(--red); flex: none; }
  .brand-name {
    color: var(--white); font-weight: 800; font-size: 34px;
    text-transform: uppercase; letter-spacing: 1px; line-height: 1; white-space: nowrap;
  }

  .header {
    position: absolute; top: 0; left: 0; width: 849px; height: 212px;
    background: var(--navy); display: flex; align-items: center; justify-content: center;
  }

  .product-photo {
    position: absolute; left: 230px; top: 255px; width: 390px; height: 320px;
    background: radial-gradient(ellipse at center, var(--photo-light) 0%, var(--photo-dark) 100%);
    border-radius: 6px;
  }

  .plan {
    position: absolute; top: 600px; left: 0; width: 849px; height: 250px;
    background: var(--red); color: var(--white); padding: 55px 0 0 28px;
  }
  .plan-title {
    font-weight: 800; font-size: 21px; text-transform: uppercase; line-height: 1.2;
    white-space: nowrap; margin-bottom: 14px;
  }
  .benefits { list-style: none; padding-left: 50px; }
  .benefits li {
    display: flex; align-items: center; gap: 12px; white-space: nowrap;
    font-weight: 800; font-size: 21px; text-transform: uppercase; line-height: 1; margin-bottom: 9px;
  }
  .benefits .num {
    width: 23px; height: 23px; border-radius: 50%; background: var(--white); color: var(--red);
    font-size: 14px; display: flex; align-items: center; justify-content: center; flex: none;
  }

  .footer {
    position: absolute; top: 875px; left: 0; width: 849px; height: 325px;
    background: var(--navy); color: var(--white); text-align: center; padding-top: 48px;
  }
  .cta-line { font-weight: 800; font-size: 30px; text-transform: uppercase; line-height: 1.5; }
  .footer .brand { margin-top: 78px; }
</style>
</head>
<body>
<main class="flyer">
  <header class="header">
    <div class="brand">
      <span class="brand-mark"></span>
      <span class="brand-name">The Watchpost Depot</span>
    </div>
  </header>

  <div class="product-photo" role="img" aria-label="Security products: a door with access control reader, monitoring screen, dome camera and bullet camera"></div>

  <section class="plan">
    <h1 class="plan-title">The price of the service plan is $299/yr and includes:</h1>
    <ol class="benefits">
      <li><span class="num">1</span>Discounted service rate of $118/hr</li>
      <li><span class="num">2</span>Free remote support ($85/hr without a plan)</li>
      <li><span class="num">3</span>Free remote training</li>
      <li><span class="num">4</span>Priority support</li>
    </ol>
  </section>

  <footer class="footer">
    <p class="cta-line">Review our website at</p>
    <p class="cta-line">www.kelvamart.com</p>
    <div class="brand">
      <span class="brand-mark"></span>
      <span class="brand-name">The Watchpost Depot</span>
    </div>
  </footer>
</main>
</body>
</html>
```